Coffee Bag Label

I need label design for both front and back of the coffee bag. I already have had many friends work on it over the past few years and have been selling coffee for two years now. I'm ready to take the next step and expand the business. I live in Nicaragua and sell a lot there, but my main focus is the States and I also want the design to be global friendly. I plan to try and get the product in Europe and Asia. I want to distribute the coffee to large and small stores for resell. I will upload some work done. I like our logo and background art as a friend actually painted it for me. I use white gloss bags and it has a valve on the front. I want the label to be squared from the valve to bottom of bag and sides. The back label can be taller and just a matching template and I can add most of the info on the farm and the coffee. I'm looking for either clean and simple or bright and colorful... I want it to stand out to people around the world as a high quality coffee. I sell single source coffee from one farm and it has all the qualities of the best coffee in the world. I would like to be able to clean up the front label and not have to have all the key features on the front and let the image sell itself. I think the main features of my coffee are that it is high altitude and single source.
Updates

I uploaded a png file of the project. It's the dark roast copycopy Added Thursday, December 04, 2014

Target Market(s)

America, Nicaragua, Europe and Asia

Industry/Entity Type

Business

Requirements
Must have
• The psd file. Either one main label in which I have three, because I will print one for dark roast, medium roast and ground. Or, one main label with a small blank space for me to place a small sticker saying dark, medium, ground or expresso... This little sticker can be very very simple yet unique maybe? in shape... Design for labels/stickers to place on the white bag.
Nice to have
• I like my logo, but I'm open to it being cleaned up or other font options... The label could possible by odd shaped in look, but clear edges for a simple square label. I like the colors of my logo... but am open to change. Remember, my bags are gloss white.
Should not have
• Main goal is to keep all costs in printing super low, so crazy shaped or foil print is not a good idea as my costs in printing will double. I can not have design all over the bag as I can not afford to print to bag yet. We are not designing the whole coffee bag, just the label for the front and back.

```html
<!DOCTYPE html>
<html lang="en">
<head>
<meta charset="utf-8">
<title>Ridgeway Coffee – Bag Labels</title>
<link rel="stylesheet" href="https://fonts.googleapis.com/css2?family=Roboto+Slab:wght@700&family=Arimo:wght@400&family=Lobster&family=Josefin+Sans:wght@600&display=swap">
<style>
  :root {
    --brown: #4a2b1f;
    --green: #7cc242;
    --green-soft: #a9d77c;
    --green-tint: #e4f1d6;
    --blue: #3ec2d0;
    --blue-tint: #cfeef2;
    --red: #b8232f;
    --red-tint: #f6d6d6;
    --line: #d8d8d8;
    --paper: #ffffff;
  }
  * { margin: 0; padding: 0; box-sizing: border-box; }
  html, body { width: 1200px; height: 1000px; overflow: hidden; background: var(--paper); }
  .sheet { position: relative; width: 1200px; height: 1000px; font-family: "Arimo", Arial, sans-serif; color: var(--brown); }

  .bag { position: absolute; background: var(--paper); border: 1px solid var(--line); }
  .bag-band { position: absolute; left: 0; right: 0; top: 0; }
  .bag-band.green { background: var(--green); }
  .bag-band.blue { background: var(--blue); }
  .bag-band.red { background: var(--red); }
  .hang-hole { position: absolute; border: 1px solid #c8c8c8; border-radius: 50%; background: var(--paper); }

  .label { position: absolute; border: 1px solid var(--line); overflow: hidden; background: var(--paper); }
  .bean-field { position: absolute; left: 0; right: 0; bottom: 0; }
  .bean-field.green { background: linear-gradient(to bottom, rgba(255,255,255,0) 0%, var(--green-tint) 45%, var(--green-soft) 100%); }
  .bean-field.blue { background: linear-gradient(to bottom, rgba(255,255,255,0) 0%, var(--blue-tint) 45%, #8fd9e2 100%); }
  .bean-field.red { background: linear-gradient(to bottom, rgba(255,255,255,0) 0%, var(--red-tint) 45%, #e49a9a 100%); }

  .brand { position: absolute; left: 0; right: 0; text-align: center; font-family: "Roboto Slab", Georgia, serif; font-weight: 700; color: var(--brown); }
  .brand-rule { position: absolute; height: 2px; background: var(--brown); }
  .brand-line { display: block; line-height: 1; }

  .variety-badge { position: absolute; border-radius: 50%; background: var(--paper); border: 3px solid var(--brown); box-shadow: 0 0 0 6px var(--paper), 0 0 0 7px #ddd; text-align: center; }
  .variety-badge .ring-text { position: absolute; left: 0; right: 0; font-family: "Josefin Sans", sans-serif; font-weight: 600; letter-spacing: 1.5px; text-transform: uppercase; color: var(--brown); }
  .variety-badge .variety { position: absolute; left: 0; right: 0; font-family: "Lobster", cursive; color: var(--brown); line-height: 1; }

  .net-weight { position: absolute; left: 0; right: 0; text-align: center; color: var(--brown); }

  .tagline { position: absolute; left: 0; right: 0; top: 266px; text-align: center; font-family: "Roboto Slab", Georgia, serif; font-weight: 700; font-size: 12px; letter-spacing: 3px; }
  .farm-story { position: absolute; left: 26px; top: 334px; width: 166px; font-size: 11.4px; line-height: 17px; text-align: justify; }
  .nutrition { position: absolute; left: 212px; top: 337px; width: 187px; font-size: 10.5px; border-collapse: collapse; }
  .nutrition caption { background: var(--brown); color: var(--paper); height: 24px; line-height: 24px; font-size: 11px; }
  .nutrition td { height: 17px; padding: 0; }
  .nutrition td.value { text-align: center; width: 52px; border-left: 1px solid var(--brown); }
  .nutrition tfoot td { background: var(--brown); color: var(--paper); text-align: center; font-size: 9px; height: 18px; }
  .nutrition tbody tr:first-child td { padding-top: 6px; }
  .nutrition tbody tr:last-child td { padding-bottom: 5px; }
</style>
</head>
<body>
<main class="sheet">

  <!-- Front: ground -->
  <section class="bag" style="left:0;top:0;width:479px;height:1000px;" aria-label="Front label, ground beans">
    <div class="bag-band green" style="height:109px;" role="img" aria-label="Green band with a pattern of light coffee beans"></div>
    <div class="hang-hole" style="left:195px;top:119px;width:88px;height:88px;"></div>
    <div class="label" style="left:26px;top:230px;width:427px;height:739px;">
      <div class="bean-field green" style="top:280px;" role="img" aria-label="Scattered green coffee beans growing denser toward the bottom"></div>
      <div class="brand-rule" style="left:48px;width:328px;top:35px;"></div>
      <h1 class="brand" style="top:52px;">
        <span class="brand-line" style="font-size:50px;letter-spacing:1px;">RIDGEWAY</span>
        <span class="brand-line" style="font-size:96px;margin-top:4px;">Coffee</span>
      </h1>
      <div class="brand-rule" style="left:48px;width:328px;top:222px;"></div>
      <div class="variety-badge" style="left:120px;top:380px;width:190px;height:190px;">
        <span class="ring-text" style="top:22px;font-size:8px;">Premium Quality Bean</span>
        <span class="variety" style="top:48px;font-size:38px;">Ground<br>&nbsp;&nbsp;Beans</span>
        <span class="ring-text" style="bottom:20px;font-size:7px;">Matagalpa | Nicaragua</span>
      </div>
      <p class="net-weight" style="top:712px;font-size:12px;">NET WT 16 oz 1lb. (460 grams)</p>
    </div>
  </section>

  <!-- Back -->
  <section class="bag" style="left:478px;top:0;width:479px;height:1000px;" aria-label="Back label">
    <div class="bag-band green" style="height:109px;" role="img" aria-label="Green band with a pattern of light coffee beans"></div>
    <div class="label" style="left:26px;top:230px;width:427px;height:739px;">
      <div class="bean-field green" style="top:280px;" role="img" aria-label="Scattered green coffee beans growing denser toward the bottom"></div>
      <p class="tagline" style="top:36px;">100% ARABICA - HIGH ALTITUDE - SHADE GROWN</p>
      <p class="farm-story" style="top:104px;">Lorem ipsum dolor sit amet, consectetur adipiscing elit, sed do eiusmod tempor incididunt ut labore et dolore magna aliqua. Ut enim ad minim veniam, quis nostrud exercitation ullamco laboris nisi ut aliquip ex ea commodo consequat.</p>
      <table class="nutrition" style="top:107px;">
        <caption>NUTRITION FACTS</caption>
        <tbody>
          <tr><td>Lorem ipsum</td><td class="value">xxx</td><td class="value">xxx</td></tr>
          <tr><td>Dolor sit amet</td><td class="value">xxx</td><td class="value">xxx</td></tr>
          <tr><td>Consectetur</td><td class="value">xxx</td><td class="value">xxx</td></tr>
          <tr><td>Adipiscing elit</td><td class="value">xxx</td><td class="value">xxx</td></tr>
          <tr><td>Do eiusmod</td><td class="value">xxx</td><td class="value">xxx</td></tr>
        </tbody>
        <tfoot><tr><td colspan="3">Lorem ipsum dolor sit amet consecte</td></tr></tfoot>
      </table>
      <div class="brand-rule" style="left:158px;width:110px;top:632px;height:1px;"></div>
      <p class="brand" style="top:638px;">
        <span class="brand-line" style="font-size:15px;">RIDGEWAY</span>
        <span class="brand-line" style="font-size:30px;">Coffee</span>
      </p>
      <div class="brand-rule" style="left:158px;width:110px;top:688px;height:1px;"></div>
    </div>
  </section>

  <!-- Front: medium roast -->
  <section class="bag" style="left:962px;top:0;width:238px;height:500px;border:none;" aria-label="Front label, medium roast">
    <div class="bag-band blue" style="height:57px;" role="img" aria-label="Blue band with a pattern of light coffee beans"></div>
    <div class="hang-hole" style="left:96px;top:60px;width:46px;height:46px;"></div>
    <div class="label" style="left:12px;top:116px;width:214px;height:374px;">
      <div class="bean-field blue" style="top:140px;" role="img" aria-label="Scattered blue coffee beans growing denser toward the bottom"></div>
      <div class="brand-rule" style="left:24px;width:166px;top:18px;height:1px;"></div>
      <h2 class="brand" style="top:27px;">
        <span class="brand-line" style="font-size:25px;">RIDGEWAY</span>
        <span class="brand-line" style="font-size:48px;margin-top:2px;">Coffee</span>
      </h2>
      <div class="brand-rule" style="left:24px;width:166px;top:112px;height:1px;"></div>
      <div class="variety-badge" style="left:59px;top:192px;width:96px;height:96px;border-width:2px;box-shadow:0 0 0 3px var(--paper),0 0 0 4px #ddd;">
        <span class="ring-text" style="top:11px;font-size:4px;letter-spacing:0.8px;">Premium Quality Bean</span>
        <span class="variety" style="top:24px;font-size:19px;">Medium<br>&nbsp;Roast</span>
        <span class="ring-text" style="bottom:10px;font-size:3.5px;letter-spacing:0.8px;">Matagalpa | Nicaragua</span>
      </div>
      <p class="net-weight" style="top:358px;font-size:6px;">NET WT 16 oz 1lb. (460 grams)</p>
    </div>
  </section>

  <!-- Front: dark roast -->
  <section class="bag" style="left:962px;top:505px;width:238px;height:495px;border:none;" aria-label="Front label, dark roast">
    <div class="bag-band red" style="height:53px;" role="img" aria-label="Red band with a pattern of light coffee beans"></div>
    <div class="hang-hole" style="left:96px;top:55px;width:46px;height:46px;"></div>
    <div class="label" style="left:12px;top:115px;width:214px;height:375px;">
      <div class="bean-field red" style="top:140px;" role="img" aria-label="Scattered red coffee beans growing denser toward the bottom"></div>
      <div class="brand-rule" style="left:24px;width:166px;top:18px;height:1px;"></div>
      <h2 class="brand" style="top:27px;">
        <span class="brand-line" style="font-size:25px;">RIDGEWAY</span>
        <span class="brand-line" style="font-size:48px;margin-top:2px;">Coffee</span>
      </h2>
      <div class="brand-rule" style="left:24px;width:166px;top:112px;height:1px;"></div>
      <div class="variety-badge" style="left:59px;top:192px;width:96px;height:96px;border-width:2px;box-shadow:0 0 0 3px var(--paper),0 0 0 4px #ddd;">
        <span class="ring-text" style="top:11px;font-size:4px;letter-spacing:0.8px;">Premium Quality Bean</span>
        <span class="variety" style="top:24px;font-size:19px;">Dark<br>&nbsp;Roast</span>
        <span class="ring-text" style="bottom:10px;font-size:3.5px;letter-spacing:0.8px;">Matagalpa | Nicaragua</span>
      </div>
      <p class="net-weight" style="top:358px;font-size:6px;">NET WT 16 oz 1lb. (460 grams)</p>
    </div>
  </section>

</main>
</body>
</html>
```